KVRo Business Cards

We need a business card design. We are a Technology (Audio Visual) design, sales and installation company. Looking for a double sided design, clean

Contact Information for Business Card

Clean, modern look, 2 sided

Font styles to use
Sans Serif

```html
<!DOCTYPE html>
<html lang="en">
<head>
<meta charset="utf-8">
<title>KVRo Business Cards</title>
<link rel="stylesheet" href="https://fonts.googleapis.com/css2?family=Roboto:wght@400;700&display=swap">
<style>
  :root {
    --stage: #9c9c9c;
    --navy: #1b3142;
    --navy-soft: #22394b;
    --orange: #f7941d;
    --ink: #1e1e1e;
    --rule: #9a9a9a;
    --white: #ffffff;
  }
  html, body {
    margin: 0;
    width: 1200px;
    height: 1200px;
    overflow: hidden;
    background: var(--stage);
    font-family: "Roboto", Arial, sans-serif;
  }
  .canvas { position: relative; width: 1200px; height: 1200px; }
  .card {
    position: absolute;
    border-radius: 18px;
    overflow: hidden;
  }
  .card--front {
    left: 201px; top: 304px; width: 369px; height: 593px;
    background: var(--navy);
  }
  .front-texture {
    position: absolute; inset: 0;
    background: radial-gradient(ellipse at 50% 55%, var(--navy-soft) 0%, var(--navy) 70%);
  }
  .wordmark {
    position: absolute; left: 0; right: 0;
    text-align: center;
    font-weight: 700;
    letter-spacing: -2px;
    line-height: 1;
  }
  .card--front .wordmark {
    top: 268px; font-size: 134px; color: var(--white);
  }
  .card--back {
    left: 599px; top: 303px; width: 364px; height: 594px;
    background: var(--white);
  }
  .card--back .wordmark {
    top: 110px; font-size: 126px; color: var(--navy);
  }
  .row {
    position: absolute; left: 0; right: 0;
    text-align: center;
    white-space: nowrap;
  }
  .person-name {
    top: 324px; font-size: 34px; line-height: 34px;
    font-weight: 700; color: var(--navy);
  }
  .person-title {
    top: 355px; font-size: 20px; line-height: 22px;
    color: var(--orange);
  }
  .icon-bar {
    top: 388px; height: 26px;
    display: flex; justify-content: center; align-items: center; gap: 5px;
  }
  .icon-bar .rule { width: 30px; height: 1px; background: var(--rule); margin: 0 5px; }
  .icon {
    width: 25px; height: 25px; border-radius: 3px; background: var(--navy);
    display: flex; align-items: center; justify-content: center;
  }
  .contact {
    top: 425px; font-size: 18px; line-height: 21px; color: var(--ink);
  }
  .contact .accent { color: var(--orange); }
  .divider {
    position: absolute; top: 501px; left: 104px; width: 156px; height: 1px;
    background: var(--rule);
  }
  .address {
    top: 511px; font-size: 18px; line-height: 21px; color: var(--ink);
  }
</style>
</head>
<body>
<main class="canvas">
  <section class="card card--front" aria-label="Card front">
    <div class="front-texture" role="img" aria-label="Faint repeated letter pattern in dark navy tones"></div>
    <div class="wordmark">KVRo</div>
  </section>

  <section class="card card--back" aria-label="Card back">
    <div class="wordmark">KVRo</div>
    <div class="row person-name">DANIEL HART</div>
    <div class="row person-title">MANAGING DIRECTOR</div>
    <div class="row icon-bar">
      <span class="rule"></span>
      <span class="icon" aria-label="Phone">
        <svg width="17" height="15" viewBox="0 0 17 15"><path d="M1 5 Q8.5 0 16 5 L14 7 L11.5 5.5 L11.5 4 Q8.5 3 5.5 4 L5.5 5.5 L3 7 Z" fill="#fff"/><rect x="4" y="7.5" width="9" height="6.5" rx="1" fill="#fff"/><circle cx="8.5" cy="10.7" r="1.6" fill="#1b3142"/></svg>
      </span>
      <span class="icon" aria-label="Email">
        <svg width="17" height="12" viewBox="0 0 17 12"><rect x="0.75" y="0.75" width="15.5" height="10.5" fill="none" stroke="#fff" stroke-width="1.3"/><path d="M1 1 L8.5 7 L16 1 M1 11 L6.5 5.5 M16 11 L10.5 5.5" fill="none" stroke="#fff" stroke-width="1.1"/></svg>
      </span>
      <span class="icon" aria-label="Web">
        <svg width="16" height="16" viewBox="0 0 16 16"><circle cx="8" cy="8" r="7" fill="#fff"/><path d="M4 4 Q7 3 7.5 6 Q6 8 4.5 7.5 Z M9 9 Q12 8.5 12 11 Q10.5 13 9.5 12 Z" fill="#1b3142"/></svg>
      </span>
      <span class="rule"></span>
    </div>
    <div class="row contact">
      (555)014-2270<br>
      SALES@KVRO.TECH<br>
      WWW.<span class="accent">KVRO</span>.TECH
    </div>
    <div class="divider"></div>
    <div class="row address">
      1180 LARKFIELD CT. SUITE 200<br>
      RIVERTON, GEORGIA 30599
    </div>
  </section>
</main>
</body>
</html>
```